We are a wholesale and b2b custom furniture company. You can view our website at www.corvalinteriors.com. One of our specialties is designing/manufacturing furniture for lobbies and public spaces in shopping malls.

We will be sending this postcard to the general managers of higher-end shopping malls in an effort to have them order furniture from for their lobbies/public spaces. Time is running out for them to order for delivery before "Black Friday" so the timing of the postcard is important.

We would like a large postcard, 6" high x 8.75" wide.

In general, we like clean designs with some white space. High-end, sophisticated, modern. Nothing too fussy.

Front of postcard:
Photo(s) of mall installations. Text on front : “Is your mall's furniture ready for holiday shoppers?”

Back of postcard:
The back needs to have space reserved for a stamp/mailing address. Also a few figure-on-ground (cut out images of furniture on white background) thumbnail photos of furniture on the back near our text would be nice. I've attached several, so choose the images that work for the design...no need to use all of the photos.

Text on back of postcard:

We can help!

- Durable sofas, chairs, sectionals, modular seating, ottomans, and tables.
-Easy to customize for your unique environment.
- USB/ power/ charging options.
- Order now for delivery before Black Friday! (**Bold?)

Call us at 888.527.3190

(logo) C O R V A L M O S T E N F U R N I T U R E
www.corvalinteriors.com
Made with pride in California.

*END*

Target Market(s)

General managers of high-end shopping malls/ shopping centers.

Industry/Entity Type

It Company

Font styles to use
Sans Serif

Colors
acd036
ffffff
faa54b
f78f20

Requirements
Must have
• The text that I outlined in the project description above.
Nice to have
• I have included a draft idea of a layout...would like to see what other designers come up with, but this was a layout idea of the front/back.

```html
<!DOCTYPE html>
<html lang="en">
<head>
<meta charset="utf-8">
<title>Corval Mosten Furniture – Holiday Mall Postcard</title>
<link rel="stylesheet" href="https://fonts.googleapis.com/css2?family=Montserrat:wght@500;600;700&family=Open+Sans:wght@400;600&display=swap">
<style>
  :root {
    --lime: #acd036;
    --white: #ffffff;
    --orange-light: #faa54b;
    --orange: #f78f20;
    --ink: #2d2d2d;
    --ink-soft: #444444;
    --divider: #cfcfcf;
    --page: #ece8e1;
  }
  * { box-sizing: border-box; margin: 0; padding: 0; }
  html, body { width: 1200px; height: 913px; overflow: hidden; }
  body {
    background: var(--page);
    position: relative;
    font-family: "Open Sans", Arial, sans-serif;
    color: var(--ink);
  }
  .postcard {
    position: absolute;
    width: 600px;
    height: 411px;
    background: var(--white);
    box-shadow: 0 6px 18px rgba(0,0,0,.18);
    overflow: hidden;
  }
  .postcard--front { left: 60px; top: 40px; }
  .postcard--back { left: 540px; top: 470px; }

  /* Front */
  .photo { position: absolute; }
  .photo--sofa { left: 8px; top: 8px; width: 350px; height: 242px;
    background: linear-gradient(135deg, #b3aba4 0%, #8fa35f 45%, #7d9a4c 60%, #c9c2bb 100%); }
  .photo--ottomans { left: 363px; top: 8px; width: 229px; height: 152px;
    background: linear-gradient(90deg, #c84a1f 0%, #d8d6d2 50%, #1f5d9a 100%); }
  .photo--storefront { left: 363px; top: 165px; width: 229px; height: 85px;
    background: linear-gradient(180deg, #6e6152 0%, #c9b79c 100%); }
  .photo--foodcourt { left: 8px; top: 255px; width: 205px; height: 148px;
    background: linear-gradient(160deg, #8a5a3b 0%, #5e6e3e 45%, #b8aea0 100%); }
  .photo--lounge { left: 218px; top: 255px; width: 374px; height: 148px;
    background: linear-gradient(160deg, #d7cfc3 0%, #b6553d 45%, #e6dfd3 100%); }

  .headline-frame {
    position: absolute; left: 235px; top: 145px; width: 250px; height: 150px;
    border: 2px solid rgba(255,255,255,.9);
  }
  .headline {
    position: absolute; left: 250px; top: 160px; width: 250px; height: 150px;
    background: rgba(255,255,255,.86);
    display: flex; flex-direction: column; justify-content: center; align-items: center;
    font-family: "Montserrat", Arial, sans-serif; font-weight: 600;
    color: #3a3a3a; text-transform: uppercase; line-height: 1.12; text-align: center;
  }
  .headline .sm { font-size: 15px; }
  .headline .lg { font-size: 24px; }

  /* Back */
  .mailing-divider { position: absolute; left: 432px; top: 0; width: 3px; height: 100%; background: var(--divider); }
  .thumbs { position: absolute; left: 26px; top: 68px; display: flex; gap: 14px; }
  .thumb { width: 66px; height: 72px; border-radius: 6px; }
  .thumb--armchair-brown { background: linear-gradient(180deg, #6b5a52, #4f4039); }
  .thumb--armchair-green { background: linear-gradient(180deg, #b6d45a, #8fb03a); }
  .thumb--armchair-orange { background: linear-gradient(180deg, #f78f20, #d9741a); }
  .thumb--loveseat { background: linear-gradient(180deg, #e6e1d6, #b8ad9c); }
  .thumb--modular { background: linear-gradient(180deg, #4a3a33 0%, #9aa3a8 55%, #f5b21c 100%); }

  .tag {
    position: absolute; left: 118px; top: 158px;
    background: var(--orange); color: var(--white);
    font-family: "Montserrat", Arial, sans-serif; font-weight: 700; font-size: 27px;
    padding: 2px 12px 4px;
  }
  .benefits { position: absolute; left: 34px; top: 208px; width: 390px; list-style: none; font-size: 13.5px; line-height: 1.35; color: var(--ink); }
  .benefits li { padding-left: 14px; position: relative; }
  .benefits li::before { content: "•"; position: absolute; left: 0; }
  .deadline {
    position: absolute; left: 0; top: 288px; width: 432px; height: 32px;
    background: var(--lime); color: var(--white);
    font-family: "Montserrat", Arial, sans-serif; font-weight: 600; font-size: 14px;
    text-transform: uppercase; display: flex; align-items: center; padding-left: 22px;
  }
  .call { position: absolute; left: 0; top: 330px; width: 432px; text-align: center;
    font-family: "Montserrat", Arial, sans-serif; font-weight: 600; font-size: 21px; color: #333; }
  .brand { position: absolute; left: 78px; top: 366px; display: flex; gap: 10px; align-items: flex-end; }
  .brand__mark { width: 38px; height: 38px; background: var(--lime); }
  .brand__text { font-size: 11px; line-height: 1.2; color: var(--ink-soft); }
  .brand__name { font-size: 11px; letter-spacing: 1.2px; color: var(--ink-soft); }
</style>
</head>
<body>

<section class="postcard postcard--front" aria-label="Postcard front">
  <div class="photo photo--sofa" role="img" aria-label="Curved green sectional sofa in a mall atrium with round side tables"></div>
  <div class="photo photo--ottomans" role="img" aria-label="Round orange, white and blue ottomans"></div>
  <div class="photo photo--storefront" role="img" aria-label="Mall storefront behind a lounge seating area"></div>
  <div class="photo photo--foodcourt" role="img" aria-label="Busy mall food court with seating and shoppers, seen from above"></div>
  <div class="photo photo--lounge" role="img" aria-label="Mall lounge with rust armchairs, cream ottomans and round tables"></div>
  <div class="headline-frame"></div>
  <h1 class="headline">
    <span class="sm">Is your mall's</span>
    <span><span class="lg">Furniture</span> <span class="sm">ready</span></span>
    <span><span class="sm">for</span> <span class="lg">Holiday</span></span>
    <span class="lg">Shoppers?</span>
  </h1>
</section>

<section class="postcard postcard--back" aria-label="Postcard back">
  <div class="thumbs">
    <div class="thumb thumb--armchair-brown" role="img" aria-label="Brown upholstered armchair"></div>
    <div class="thumb thumb--armchair-green" role="img" aria-label="Green lounge chair on metal sled base"></div>
    <div class="thumb thumb--armchair-orange" role="img" aria-label="Orange wingback armchair"></div>
    <div class="thumb thumb--loveseat" role="img" aria-label="Cream loveseat with wood arms"></div>
    <div class="thumb thumb--modular" role="img" aria-label="Modular bench seating with grey and yellow cushions"></div>
  </div>
  <h2 class="tag">We can help!</h2>
  <ul class="benefits">
    <li>Durable sofas, chairs, sectionals, modular seating, ottomans, and tables.</li>
    <li>Easy to customize for your unique environment.</li>
    <li>USB/ power/ charging options.</li>
  </ul>
  <p class="deadline">Order now for delivery before Black Friday!</p>
  <p class="call">Call us at 888.527.3190</p>
  <div class="brand">
    <div class="brand__mark"></div>
    <div class="brand__text">
      <div class="brand__name">C O R V A L M O S T E N F U R N I T U R E</div>
      <div>www.corvalinteriors.com</div>
      <div>Made with pride in California.</div>
    </div>
  </div>
  <div class="mailing-divider"></div>
</section>

</body>
</html>
```